Free word Download template and Blog Design template

Looking for a free dowload template and blog template that we can use over and again. To see our current look, check out our website at www.velmarcrest.com.au. Further, other design docs attached. We would like to make this one a little less formal, although using similar branding.
Updates

Please note this design will be used as a template for content that can be dowloaded by a user.

Industry/Entity Type

Consulting

Requirements
Must have
• My project must be a word template

```html
<!DOCTYPE html>
<html lang="en">
<head>
<meta charset="utf-8">
<title>Velmar Crest – Our Blogs</title>
<link href="https://fonts.googleapis.com/css2?family=Arimo:wght@400;700&family=Marcellus&family=Open+Sans:wght@600;700;800&display=swap" rel="stylesheet">
<style>
:root{
  --navy:#0f2a6e;
  --gold:#b59d5f;
  --ink:#1b1b1b;
  --muted:#555;
  --page-light:#8596c0;
  --footer:#111111;
  --white:#ffffff;
}
*{margin:0;padding:0;box-sizing:border-box}
html,body{width:1200px;height:2448px;overflow:hidden;background:var(--white);font-family:"Arimo",Arial,sans-serif;color:var(--ink)}
.page{position:relative;width:1200px;height:2448px}
.topline{height:4px;background:var(--gold)}
.site-header{height:110px;display:flex;align-items:center;padding:0 110px 0 112px;justify-content:space-between}
.brand{font-family:"Marcellus",serif;font-size:31px;letter-spacing:1px;color:var(--navy);padding-top:14px}
.main-nav{display:flex;gap:62px}
.main-nav a{font-weight:700;font-size:16px;color:var(--ink);text-decoration:none;letter-spacing:.3px}
.hero{position:relative;height:414px;background:linear-gradient(135deg,#12317f 0%,#0e2a72 50%,#0b2466 100%);color:var(--white);text-align:center}
.hero h1{font-family:"Open Sans",sans-serif;font-weight:800;font-size:52px;letter-spacing:3px;padding-top:104px}
.hero p{font-size:18px;line-height:38px;margin-top:12px}
.hero .wave{position:absolute;left:0;bottom:-1px;width:1200px;height:90px}
.blog-grid{position:absolute;top:595px;left:98px;display:grid;grid-template-columns:repeat(3,314px);column-gap:31px;row-gap:58px}
.post-card{position:relative;height:426px;background:var(--white);border-radius:16px;box-shadow:0 6px 22px rgba(0,0,0,.08);overflow:hidden}
.post-image{height:216px}
.post-body{padding:34px 12px 0 28px}
.post-meta{display:flex;align-items:center;gap:8px;font-size:13px;color:var(--muted)}
.post-meta svg{width:14px;height:14px}
.post-meta .author{margin-left:14px}
.post-title{font-family:"Open Sans",sans-serif;font-weight:600;font-size:13px;letter-spacing:1px;line-height:26px;text-transform:uppercase;margin-top:18px;color:var(--ink)}
.post-excerpt{font-size:11px;line-height:25px;color:var(--muted);margin-top:8px;padding-right:6px}
.read-more{position:absolute;right:0;bottom:0;width:44px;height:40px;background:var(--gold);border-top-left-radius:40px;display:flex;align-items:center;justify-content:center;padding:8px 0 0 8px}
.pagination{position:absolute;top:2043px;left:487px;display:flex;gap:15px}
.pagination span{width:45px;height:45px;border-radius:3px;background:var(--page-light);color:var(--white);font-weight:700;font-size:13px;display:flex;align-items:center;justify-content:center}
.pagination .current{background:var(--navy)}
.site-footer{position:absolute;top:2164px;left:0;width:1200px;height:284px;background:var(--footer);color:var(--white);text-align:center}
.site-footer .brand{color:var(--white);padding-top:80px;font-size:31px}
.footer-nav{display:flex;justify-content:center;gap:54px;margin-top:22px}
.footer-nav a,.footer-nav a:visited{color:var(--white);text-decoration:none;font-size:13.5px}
.social{display:flex;justify-content:center;gap:11px;margin-top:26px}
.social span{width:31px;height:31px;background:var(--gold);border-radius:2px}
.copyright{font-size:11px;margin-top:16px}
</style>
</head>
<body>
<div class="page">
  <div class="topline"></div>
  <header class="site-header">
    <div class="brand">VELMAR CREST</div>
    <nav class="main-nav">
      <a href="#">HOME</a><a href="#">SERVICES</a><a href="#">OUR TEAM</a><a href="#">INSIGHTS</a><a href="#">CONTACT US</a>
    </nav>
  </header>

  <section class="hero" role="img" aria-label="Overhead photo of business people meeting at a table, tinted navy blue">
    <h1>OUR BLOGS</h1>
    <p>Explore our resources and stay informed on the latest developments on Probity, Workplace<br>Investigations, Dispute Resolution &amp; Training</p>
    <svg class="wave" viewBox="0 0 1200 90" preserveAspectRatio="none"><path d="M0 90 C250 80 420 6 600 2 C780 -2 950 70 1200 86 L1200 90 Z" fill="#ffffff"/></svg>
  </section>

  <main class="blog-grid">
    <article class="post-card"><div class="post-image" role="img" aria-label="Businessman reading a newspaper with coffee" style="background:linear-gradient(135deg,#c9ccd0,#3a4150)"></div>
      <div class="post-body"><div class="post-meta"><svg viewBox="0 0 14 14"><rect x="1" y="2.5" width="12" height="10.5" fill="none" stroke="#0f2a6e" stroke-width="1.5"/><rect x="1" y="2.5" width="12" height="3" fill="#0f2a6e"/><path d="M4 1v3M10 1v3" stroke="#0f2a6e" stroke-width="1.5"/></svg>28 February<svg class="author" viewBox="0 0 14 14"><circle cx="7" cy="4" r="3.2" fill="#0f2a6e"/><path d="M1 14c0-4 2.7-6 6-6s6 2 6 6z" fill="#0f2a6e"/></svg>By Ashford</div>
      <h2 class="post-title">The Story That Won’t Go Away</h2>
      <p class="post-excerpt">The Integrity of Grants Administration is again in the News. On 28 February, the Harbourline audit office announced it had issued a report</p></div>
      <div class="read-more"><svg width="14" height="8" viewBox="0 0 14 8"><path d="M0 4h11M8 1l3 3-3 3" stroke="#fff" stroke-width="1.6" fill="none"/></svg></div></article>

    <article class="post-card"><div class="post-image" role="img" aria-label="Man in a suit signing a document at a desk" style="background:linear-gradient(135deg,#dfe3ea,#2d3444)"></div>
      <div class="post-body"><div class="post-meta"><svg viewBox="0 0 14 14"><rect x="1" y="2.5" width="12" height="10.5" fill="none" stroke="#0f2a6e" stroke-width="1.5"/><rect x="1" y="2.5" width="12" height="3" fill="#0f2a6e"/><path d="M4 1v3M10 1v3" stroke="#0f2a6e" stroke-width="1.5"/></svg>28 February<svg class="author" viewBox="0 0 14 14"><circle cx="7" cy="4" r="3.2" fill="#0f2a6e"/><path d="M1 14c0-4 2.7-6 6-6s6 2 6 6z" fill="#0f2a6e"/></svg>By Ashford</div>
      <h2 class="post-title">Some Rules Are Made To Be Broken</h2>
      <p class="post-excerpt">The risks of bypassing established tendering processes are currently being played out in a public anti-corruption probe in the Australian</p></div>
      <div class="read-more"><svg width="14" height="8" viewBox="0 0 14 8"><path d="M0 4h11M8 1l3 3-3 3" stroke="#fff" stroke-width="1.6" fill="none"/></svg></div></article>

    <article class="post-card"><div class="post-image" role="img" aria-label="Hand balancing a wooden seesaw with stacks of coins" style="background:linear-gradient(135deg,#e8dcd2,#c9a890)"></div>
      <div class="post-body"><div class="post-meta"><svg viewBox="0 0 14 14"><rect x="1" y="2.5" width="12" height="10.5" fill="none" stroke="#0f2a6e" stroke-width="1.5"/><rect x="1" y="2.5" width="12" height="3" fill="#0f2a6e"/><path d="M4 1v3M10 1v3" stroke="#0f2a6e" stroke-width="1.5"/></svg>28 February<svg class="author" viewBox="0 0 14 14"><circle cx="7" cy="4" r="3.2" fill="#0f2a6e"/><path d="M1 14c0-4 2.7-6 6-6s6 2 6 6z" fill="#0f2a6e"/></svg>By Ashford</div>
      <h2 class="post-title">Value For Money Is Your Best<br>Defence</h2>
      <p class="post-excerpt">What is Value for Money When it Comes to Your Procurement?</p></div>
      <div class="read-more"><svg width="14" height="8" viewBox="0 0 14 8"><path d="M0 4h11M8 1l3 3-3 3" stroke="#fff" stroke-width="1.6" fill="none"/></svg></div></article>

    <article class="post-card"><div class="post-image" role="img" aria-label="Champagne being poured at an office party" style="background:linear-gradient(135deg,#eeeae2,#9a9184)"></div>
      <div class="post-body"><div class="post-meta"><svg viewBox="0 0 14 14"><rect x="1" y="2.5" width="12" height="10.5" fill="none" stroke="#0f2a6e" stroke-width="1.5"/><rect x="1" y="2.5" width="12" height="3" fill="#0f2a6e"/><path d="M4 1v3M10 1v3" stroke="#0f2a6e" stroke-width="1.5"/></svg>28 February<svg class="author" viewBox="0 0 14 14"><circle cx="7" cy="4" r="3.2" fill="#0f2a6e"/><path d="M1 14c0-4 2.7-6 6-6s6 2 6 6z" fill="#0f2a6e"/></svg>By Ashford</div>
      <h2 class="post-title">Deck The Halls And Know Your<br>Rights</h2>
      <p class="post-excerpt">The work Christmas party is an Australian tradition. More often than not, it is the biggest event</p></div>
      <div class="read-more"><svg width="14" height="8" viewBox="0 0 14 8"><path d="M0 4h11M8 1l3 3-3 3" stroke="#fff" stroke-width="1.6" fill="none"/></svg></div></article>

    <article class="post-card"><div class="post-image" role="img" aria-label="Hands holding wooden blocks reading conflict of interest" style="background:linear-gradient(135deg,#f4f4f4,#d9b98a)"></div>
      <div class="post-body"><div class="post-meta"><svg viewBox="0 0 14 14"><rect x="1" y="2.5" width="12" height="10.5" fill="none" stroke="#0f2a6e" stroke-width="1.5"/><rect x="1" y="2.5" width="12" height="3" fill="#0f2a6e"/><path d="M4 1v3M10 1v3" stroke="#0f2a6e" stroke-width="1.5"/></svg>28 February<svg class="author" viewBox="0 0 14 14"><circle cx="7" cy="4" r="3.2" fill="#0f2a6e"/><path d="M1 14c0-4 2.7-6 6-6s6 2 6 6z" fill="#0f2a6e"/></svg>By Ashford</div>
      <h2 class="post-title">Clearing The Fog</h2>
      <p class="post-excerpt">Not all conflicts of interest are bad. Rather, it’s the way they are disclosed, identified and managed that determine how much harm they can inflict.</p></div>
      <div class="read-more"><svg width="14" height="8" viewBox="0 0 14 8"><path d="M0 4h11M8 1l3 3-3 3" stroke="#fff" stroke-width="1.6" fill="none"/></svg></div></article>

    <article class="post-card"><div class="post-image" role="img" aria-label="Hands leafing through a stack of documents" style="background:linear-gradient(135deg,#4a505a,#1e2228)"></div>
      <div class="post-body"><div class="post-meta"><svg viewBox="0 0 14 14"><rect x="1" y="2.5" width="12" height="10.5" fill="none" stroke="#0f2a6e" stroke-width="1.5"/><rect x="1" y="2.5" width="12" height="3" fill="#0f2a6e"/><path d="M4 1v3M10 1v3" stroke="#0f2a6e" stroke-width="1.5"/></svg>28 February<svg class="author" viewBox="0 0 14 14"><circle cx="7" cy="4" r="3.2" fill="#0f2a6e"/><path d="M1 14c0-4 2.7-6 6-6s6 2 6 6z" fill="#0f2a6e"/></svg>By Ashford</div>
      <h2 class="post-title">Dial Before You Dig</h2>
      <p class="post-excerpt">A simple four-word phrase neatly summarises the essential due diligence excavation contractors must perform before breaking ground</p></div>
      <div class="read-more"><svg width="14" height="8" viewBox="0 0 14 8"><path d="M0 4h11M8 1l3 3-3 3" stroke="#fff" stroke-width="1.6" fill="none"/></svg></div></article>

    <article class="post-card"><div class="post-image" role="img" aria-label="Stressed worker in a counselling session" style="background:linear-gradient(135deg,#d8dde2,#2e4e70)"></div>
      <div class="post-body"><div class="post-meta"><svg viewBox="0 0 14 14"><rect x="1" y="2.5" width="12" height="10.5" fill="none" stroke="#0f2a6e" stroke-width="1.5"/><rect x="1" y="2.5" width="12" height="3" fill="#0f2a6e"/><path d="M4 1v3M10 1v3" stroke="#0f2a6e" stroke-width="1.5"/></svg>28 February<svg class="author" viewBox="0 0 14 14"><circle cx="7" cy="4" r="3.2" fill="#0f2a6e"/><path d="M1 14c0-4 2.7-6 6-6s6 2 6 6z" fill="#0f2a6e"/></svg>By Ashford</div>
      <h2 class="post-title">Psychosocial Hazards In The<br>Workplace</h2>
      <p class="post-excerpt">In today’s modern workplace, the focus on<br>occupational health and safety extends beyond</p></div>
      <div class="read-more"><svg width="14" height="8" viewBox="0 0 14 8"><path d="M0 4h11M8 1l3 3-3 3" stroke="#fff" stroke-width="1.6" fill="none"/></svg></div></article>

    <article class="post-card"><div class="post-image" role="img" aria-label="Envelope with a confidential document and a pen" style="background:linear-gradient(135deg,#f2f2f2,#d9a765)"></div>
      <div class="post-body"><div class="post-meta"><svg viewBox="0 0 14 14"><rect x="1" y="2.5" width="12" height="10.5" fill="none" stroke="#0f2a6e" stroke-width="1.5"/><rect x="1" y="2.5" width="12" height="3" fill="#0f2a6e"/><path d="M4 1v3M10 1v3" stroke="#0f2a6e" stroke-width="1.5"/></svg>28 February<svg class="author" viewBox="0 0 14 14"><circle cx="7" cy="4" r="3.2" fill="#0f2a6e"/><path d="M1 14c0-4 2.7-6 6-6s6 2 6 6z" fill="#0f2a6e"/></svg>By Ashford</div>
      <h2 class="post-title">Strategies For Protecting<br>Confidential Information</h2>
      <p class="post-excerpt">The recent revelations about Harlow &amp; Finch’s use of<br>information obtained while advising the federal</p></div>
      <div class="read-more"><svg width="14" height="8" viewBox="0 0 14 8"><path d="M0 4h11M8 1l3 3-3 3" stroke="#fff" stroke-width="1.6" fill="none"/></svg></div></article>

    <article class="post-card"><div class="post-image" role="img" aria-label="Person cupping a hand to the ear to listen" style="background:linear-gradient(135deg,#5a5c5e,#b88e74)"></div>
      <div class="post-body"><div class="post-meta"><svg viewBox="0 0 14 14"><rect x="1" y="2.5" width="12" height="10.5" fill="none" stroke="#0f2a6e" stroke-width="1.5"/><rect x="1" y="2.5" width="12" height="3" fill="#0f2a6e"/><path d="M4 1v3M10 1v3" stroke="#0f2a6e" stroke-width="1.5"/></svg>28 February<svg class="author" viewBox="0 0 14 14"><circle cx="7" cy="4" r="3.2" fill="#0f2a6e"/><path d="M1 14c0-4 2.7-6 6-6s6 2 6 6z" fill="#0f2a6e"/></svg>By Ashford</div>
      <h2 class="post-title">Strengthening Protections For<br>Whistleblowers</h2>
      <p class="post-excerpt">Since its introduction nearly thirty years ago, the<br>Public Interest Disclosures Act 1994 has aimed</p></div>
      <div class="read-more"><svg width="14" height="8" viewBox="0 0 14 8"><path d="M0 4h11M8 1l3 3-3 3" stroke="#fff" stroke-width="1.6" fill="none"/></svg></div></article>
  </main>

  <nav class="pagination"><span class="current">01</span><span>02</span><span>03</span><span>04</span></nav>

  <footer class="site-footer">
    <div class="brand">VELMAR CREST</div>
    <nav class="footer-nav"><a href="#">HOME</a><a href="#">SERVICES</a><a href="#">OUR TEAM</a><a href="#">INSIGHTS</a><a href="#">CONTACT US</a></nav>
    <div class="social"><span></span><span></span><span></span></div>
    <p class="copyright">(C) Copyright 2024 | All Rights Reserved</p>
  </footer>
</div>
</body>
</html>
```